Web & Logo Design Project

STOP...please read entire brief before submitting :)
(designers have been submitting random designs)

Global Craft Transfer Society USA seeks new website.
GCTSUSA.org

Who we are: A brand new company that brings top student designers to Los Angeles for the summer to learn English and intern at some of the best design firms in Hollywood.

Clients: Students aged 19-25 and their parents

Objectives: A professional and creative site that communicates design, education, and a 4 star experience.

- Should be professional so that students trust the company
- Should encourage students to apply
- Needs to communicate creativity & design
- Should focus on the professional design studio experience and the location: Los Angeles & Hollywood!

What we need: Logo + Website

Logo should work small as a favicon and large when used on posters.
It should have an icon and the words GCTS USA.
Icon should work with and without the words.
Logo can be an abstract shape or a stylized light bulb.
A folder of possible logo ideas can be downloaded below.
Red White & Blue can be used, or stars. Eventually we will add other countries so logo should be able to change accordingly.

Website MUST have an animated slideshow of design pictures and location shots for the landing page. It should give students and idea of what to expect on the program. Please select your favorite pics from all of the photos attached.

Site should also be easy to maintain and optimize.
Should be easy to upload photos and add companies to the company page.

Please submit:

Logo
Landing Page
The Program Page
The Companies Page

Winner of the project will be asked to program the entire site an upload site to the server. We would also like to work with the designer in the future to upload and change the site. The final site will be in 3 languages (French, English, Spanish).

Other sites in our industry:
www.trovanbursars.com
www.brightlyplacements.com

Files Provided:
Web layout in PDF format
Sample photos. (We encourage you to source additional photos.)
Logo examples
Website text in word doc. (coming soon)

If you have any questions please feel free to message us.

Target Market(s)

Students 19-25 and their parents

Industry/Entity Type

Education

Requirements
Must have
• Please use the Web Layout PDF provided and the content doc instead of lorem ipsum or Greek text with random buttons and navigation.

Animated slideshow of project photos on landing page.
Application form, Employer form, contact form
Should not have
• Should not look like an American flag. A nod to the fact that we are bringing students to the US for the summer is great, but this is not a political website. This is a site for designers that want to travel and experience Hollywood.

```html
<!DOCTYPE html>
<html lang="en">
<head>
<meta charset="utf-8">
<title>GCTS USA – The Program</title>
<link href="https://fonts.googleapis.com/css2?family=Arimo:ital,wght@0,400;0,700;1,400&display=swap" rel="stylesheet">
<style>
:root{
  --header-bg:#262626;
  --nav-bg:#24a3bf;
  --nav-active:#16809b;
  --nav-divider:#1b8aa4;
  --teal:#1a7a96;
  --orange:#e55a12;
  --body-text:#333;
  --muted:#666;
  --alert:#c8151b;
  --tab-active:#86d0df;
  --tab-bg:#efefef;
  --panel-bg:#f5f5f5;
  --footer-bg:#222;
  --footer-text:#ccc;
  --brand-dot:#e0312a;
}
*{box-sizing:border-box;margin:0;padding:0}
html,body{width:1092px;height:1200px;overflow:hidden;background:#fff;font-family:Arimo,Arial,sans-serif;color:var(--body-text)}
.site-header{height:119px;background:var(--header-bg);position:relative;border-bottom:2px solid #111}
.lang-switch{position:absolute;left:84px;top:52px;display:flex;gap:13px}
.lang-switch svg{display:block}
.brand{position:absolute;left:0;right:0;top:40px;display:flex;align-items:center;justify-content:center;gap:12px}
.brand-mark{width:26px;height:26px;border-radius:50%;background:var(--brand-dot)}
.brand-name{font-size:30px;font-weight:700;color:#fff;line-height:1}
.contact-btn{position:absolute;right:82px;top:45px;height:24px;padding:0 10px 0 4px;background:#111;border-radius:12px;color:#fff;font-size:14px;font-weight:700;display:flex;align-items:center;gap:6px}
.main-nav{height:58px;background:var(--nav-bg);display:flex;padding-left:82px;border-bottom:1px solid #1690ab}
.main-nav a{color:#fff;text-decoration:none;font-weight:700;font-size:14px;display:flex;align-items:center;justify-content:center;border-left:1px solid var(--nav-divider);height:100%}
.main-nav a:last-child{border-right:1px solid var(--nav-divider)}
.main-nav a.active{background:var(--nav-active)}
.page{padding:32px 82px 0 83px}
h1{font-weight:400;font-size:25px;color:var(--teal)}
h2{font-weight:400;font-size:19px;color:var(--orange);margin-top:26px}
.lead{font-style:italic;font-size:15px;color:var(--muted);line-height:25px;margin-top:14px;letter-spacing:-0.1px}
.overview{display:flex;justify-content:space-between;margin-top:10px}
.overview-text{width:560px;font-size:12.2px;line-height:21px}
.overview-text p{margin-bottom:8px}
.photo-frame{width:348px;height:198px;background:#ddd;padding:6px}
.photo{width:100%;height:100%;background:linear-gradient(120deg,#3b2a22 0%,#6a4a3a 40%,#9bb8d8 70%,#d8e6f3 100%)}
.details{display:flex;margin-top:54px}
.tabs{width:245px;list-style:none}
.tabs li{height:39px;margin-bottom:9px;background:linear-gradient(90deg,var(--tab-bg),#fafafa);clip-path:polygon(0 0,94% 0,100% 50%,94% 100%,0 100%);display:flex;align-items:center;padding-left:20px;font-size:14.5px;color:#555}
.tabs li.active{background:var(--tab-active);color:#111}
.tab-panel{margin-left:27px;padding:18px 0 30px 28px;background:linear-gradient(90deg,#f6f6f6,#fff 140px);width:660px;font-size:12.2px;line-height:21px}
.tab-panel p{margin-bottom:9px}
.tab-panel .note{color:var(--alert);padding-left:12px;text-indent:-12px;max-width:590px}
.deadline-box{background:var(--panel-bg);width:433px;padding:14px 30px;margin-top:20px;color:var(--teal);font-size:15px;line-height:22px}
.deadline-box p{margin:0 0 22px;white-space:nowrap}
.deadline-box p:last-child{margin:0}
.site-footer{position:absolute;left:0;top:1043px;width:1092px;height:157px;background:var(--footer-bg);border-top:3px solid #111}
.footer-nav{display:flex;justify-content:space-between;margin:24px 82px 0 105px;font-size:12.5px;color:var(--footer-text)}
.footer-nav span.active{color:#fff}
.footer-rule{margin:24px 82px 0 83px;border-top:1px solid #3a3a3a}
.footer-bottom{display:flex;justify-content:space-between;align-items:center;margin:26px 82px 0 83px;font-size:12.5px;color:#aaa}
.social{display:flex;gap:8px}
.social span{width:24px;height:24px;border-radius:50%;background:#666;display:flex;align-items:center;justify-content:center}
</style>
</head>
<body>
<header class="site-header">
  <div class="lang-switch">
    <svg width="21" height="15" viewBox="0 0 21 15" aria-label="Français"><rect width="7" height="15" fill="#2a3d8f"/><rect x="7" width="7" height="15" fill="#fff"/><rect x="14" width="7" height="15" fill="#d52b2b"/></svg>
    <svg width="21" height="15" viewBox="0 0 21 15" aria-label="Español"><rect width="21" height="15" fill="#c8181e"/><rect y="4" width="21" height="7" fill="#f5c400"/></svg>
    <svg width="21" height="15" viewBox="0 0 21 15" aria-label="English"><rect width="21" height="15" fill="#1f3a8a"/><path d="M0 0L21 15M21 0L0 15" stroke="#fff" stroke-width="3"/><path d="M0 0L21 15M21 0L0 15" stroke="#c8181e" stroke-width="1"/><path d="M10.5 0V15M0 7.5H21" stroke="#fff" stroke-width="4"/><path d="M10.5 0V15M0 7.5H21" stroke="#c8181e" stroke-width="2"/></svg>
  </div>
  <div class="brand">
    <span class="brand-mark"></span>
    <span class="brand-name">GCTS USA</span>
  </div>
  <div class="contact-btn">
    <svg width="20" height="20" viewBox="0 0 20 20"><rect width="20" height="20" rx="4" fill="#fff"/><path d="M6 4l3 3-1.5 1.5c.8 1.8 2.2 3.2 4 4L13 11l3 3-2 2C9 15 5 11 4 6z" fill="#111"/></svg>
    Contact us
  </div>
</header>
<nav class="main-nav">
  <a style="width:171px">Apply</a>
  <a style="width:171px">Mission</a>
  <a style="width:204px">The Program</a>
  <a class="active" style="width:220px">The Companies</a>
  <a style="width:163px">FAQ</a>
</nav>
<main class="page">
  <h1>The Program</h1>
  <h2>Overview:</h2>
  <p class="lead">Receive real world work experience, improve your professional portfolio, increase your English language skills, and get a taste of what it is like to live, work, and play in Hollywood.</p>
  <div class="overview">
    <div class="overview-text">
      <p>Speaking English fluently is becoming a standard in international business and design.<br>That is why we have created a program that combines real world experience and top notch language training to give you the most practical well rounded summer program available.</p>
      <p>This program is designed so that every student receives as much personal attention as possible. That is why we only select 10-12 students. Each student will receive a guaranteed intern position at one of Los Angeles' top design, advertising, packaging, or entertainment companies.</p>
      <p>In addition we will provide each participant with premium luxury accommodations, advanced English language courses, and weekend excursions to some of the most popular sites in the Southern California region.</p>
    </div>
    <div class="photo-frame"><div class="photo" role="img" aria-label="Photo of a designer drawing a cartoon on a pen display in a studio"></div></div>
  </div>
  <section class="details">
    <ul class="tabs">
      <li class="active">How to Apply</li>
      <li>English Language Component</li>
      <li>Internship Component</li>
      <li>Dates &amp; Deadlines</li>
      <li>Housing</li>
      <li>School Credit</li>
      <li>Weekends and Excursions</li>
      <li>Program Tuition</li>
    </ul>
    <div class="tab-panel">
      <p style="margin-bottom:20px">To enter please fill out the online application form and upload your graphic design portfolio, cover letter, and CV</p>
      <p>Your design portfolio should be between 10-12 pages. Please submit a link to download your portfolio<br>or a link to your website. For examples of a good design portfolio please click here</p>
      <p>Your cover letter should explain why you want to be a designer, what area of design you are most pas-<br>sionate about, and why you would be a good candidate for the GCTS USA program.</p>
      <p class="note">*&nbsp; You should have high B1 or B2 conversational level of English at the time of the interview if you would like to be considered for the program.</p>
      <p class="note">*&nbsp; All finalists will be required to conduct a Vidlink interview in English before being accepted.</p>
      <div class="deadline-box">
        <p>All applications must be submitted by March 29, 2013.</p>
        <p>There is a non refundable application fee of $30.00</p>
      </div>
    </div>
  </section>
</main>
<footer class="site-footer">
  <div class="footer-nav">
    <span class="active">Apply</span><span>|</span><span>Mission</span><span>|</span><span>The Program</span><span>|</span><span>The Companies</span><span>|</span><span>FAQ</span><span>|</span><span>Contact</span><span>|</span><span>Legal</span>
  </div>
  <div class="footer-rule"></div>
  <div class="footer-bottom">
    <span>Copyright &nbsp;©&nbsp; 2012 &nbsp; www.gctsusa.org &nbsp;&nbsp;&nbsp; All rights reserved.</span>
    <div class="social">
      <span></span><span></span><span></span>
      <span><svg width="14" height="10" viewBox="0 0 14 10"><rect x=".5" y=".5" width="13" height="9" fill="none" stroke="#ddd"/><path d="M.5 .5L7 6 13.5 .5" fill="none" stroke="#ddd"/></svg></span>
    </div>
  </div>
</footer>
</body>
</html>
```